Modern Innovative Business Card Design

We require a nice, modern, clean business card design, ready for upload to Cardomora. Our company develops online banking software solutions for small financial insitutions. The design should be clean, professional, but yet not "corporate boring". See www.fyrolt.com for an idea of business image and profile. The design should communicate innovation, be modern and fresh, yet look professional and established.

Target Market(s)

Finance industry, bankers, entrepreneurs

Industry/Entity Type

Financial

Contact Information for Business Card

Tobias Wendlerup
CEO

FYROLT BV
Lindenwerf 38
1027 HX Amsterdam
The Netherlands

Phone: +31 20 517 8036
Direct: +31 20 604 1758
Skype: tobias.fyrolt
ceo@fyrolt.com
www.fyrolt.com

Font styles to use
Sans Serif

Requirements
Must have
• Should look clean, modern and professional. File should be ready for upload to cardomora.
Should not have
• Boring standard corporate layout

```html
<!DOCTYPE html>
<html lang="en">
<head>
<meta charset="utf-8">
<title>FYROLT Business Card</title>
<link rel="stylesheet" href="https://fonts.googleapis.com/css2?family=Arimo:wght@400&family=Libre+Baskerville:wght@700&family=Montserrat:wght@500&display=swap">
<style>
  :root {
    --lime: #8cc63f;
    --ink: #000000;
    --logo-grey: #6d6e70;
    --paper: #ffffff;
    --backdrop: #e9e7e2;
    --card-w: 540px;
    --card-h: 310px;
  }
  * { margin: 0; padding: 0; box-sizing: border-box; }
  html, body {
    width: 1200px; height: 800px; overflow: hidden;
    background: var(--backdrop);
  }
  .sheet {
    position: relative; width: 1200px; height: 800px;
    display: flex; align-items: center; justify-content: center; gap: 40px;
  }
  .card {
    position: relative; width: var(--card-w); height: var(--card-h);
    overflow: hidden; box-shadow: 0 6px 18px rgba(0,0,0,0.18);
  }
  .card-shape { position: absolute; inset: 0; width: 100%; height: 100%; }
  .wordmark {
    position: absolute;
    font-family: "Montserrat", sans-serif; font-weight: 500;
    color: var(--logo-grey); letter-spacing: 0.12em; line-height: 1;
  }
  .card-front .wordmark { left: 50px; top: 130px; font-size: 48px; }
  .card-back .wordmark { left: 28px; top: 128px; font-size: 36px; }

  .identity { position: absolute; left: 270px; top: 34px; }
  .person-name {
    font-family: "Libre Baskerville", serif; font-weight: 700;
    font-size: 23px; color: var(--ink); white-space: nowrap;
  }
  .person-role, .person-direct {
    font-family: "Arimo", sans-serif; font-size: 13px;
    color: var(--ink); line-height: 1.35;
  }
  .person-role { margin-top: 6px; }

  .contact-list {
    position: absolute; left: 300px; top: 130px; list-style: none;
    font-family: "Arimo", sans-serif; font-size: 14px; color: var(--paper);
  }
  .contact-item { display: flex; align-items: flex-start; gap: 12px; margin-bottom: 9px; line-height: 1.3; }
  .contact-icon {
    flex: none; width: 18px; height: 18px; background: var(--ink);
    display: flex; align-items: center; justify-content: center; margin-top: 0;
  }
  .contact-icon svg { width: 12px; height: 12px; }
</style>
</head>
<body>
<main class="sheet">

  <section class="card card-front" aria-label="Card front">
    <svg class="card-shape" viewBox="0 0 540 310" preserveAspectRatio="none" aria-hidden="true">
      <rect width="540" height="310" fill="var(--ink)"/>
      <rect x="300" y="0" width="240" height="310" fill="var(--lime)"/>
      <circle cx="470" cy="300" r="250" fill="var(--ink)"/>
      <rect x="0" y="0" width="300" height="310" fill="var(--ink)"/>
    </svg>
    <div class="wordmark">FYROLT</div>
  </section>

  <section class="card card-back" aria-label="Card back">
    <svg class="card-shape" viewBox="0 0 540 310" preserveAspectRatio="none" aria-hidden="true">
      <rect width="540" height="310" fill="var(--lime)"/>
      <circle cx="70" cy="110" r="200" fill="var(--ink)"/>
    </svg>
    <div class="wordmark">FYROLT</div>

    <div class="identity">
      <h1 class="person-name">Tobias Wendlerup</h1>
      <p class="person-role">CEO FYROLT BV</p>
      <p class="person-direct">+31 20 604 1758</p>
    </div>

    <ul class="contact-list">
      <li class="contact-item">
        <span class="contact-icon"><svg viewBox="0 0 12 12"><path d="M2 1h3l1 3-1.5 1a6 6 0 0 0 2.5 2.5L8 6l3 1v3a1 1 0 0 1-1 1A9 9 0 0 1 1 2a1 1 0 0 1 1-1z" fill="#fff"/></svg></span>
        <span>+31 20 517 8036</span>
      </li>
      <li class="contact-item">
        <span class="contact-icon"><svg viewBox="0 0 12 12"><path d="M6 1a3.5 3.5 0 0 1 3.5 3.5C9.5 7 6 11 6 11S2.5 7 2.5 4.5A3.5 3.5 0 0 1 6 1z" fill="#fff"/><circle cx="6" cy="4.5" r="1.3" fill="#000"/></svg></span>
        <span>Lindenwerf 38<br>1027 HX Amsterdam<br>The Netherlands</span>
      </li>
      <li class="contact-item">
        <span class="contact-icon"><svg viewBox="0 0 12 12"><rect x="1" y="2.5" width="10" height="7" fill="#fff"/><path d="M1 2.5l5 4 5-4" stroke="#000" stroke-width="1" fill="none"/></svg></span>
        <span>ceo@fyrolt.com</span>
      </li>
      <li class="contact-item">
        <span class="contact-icon"><svg viewBox="0 0 12 12"><circle cx="6" cy="6" r="4.8" fill="none" stroke="#fff" stroke-width="1.2"/><path d="M1.2 6h9.6M6 1.2c-2.5 3-2.5 6.6 0 9.6M6 1.2c2.5 3 2.5 6.6 0 9.6" stroke="#fff" stroke-width="0.9" fill="none"/></svg></span>
        <span>www.fyrolt.com</span>
      </li>
      <li class="contact-item">
        <span class="contact-icon"><svg viewBox="0 0 12 12"><circle cx="6" cy="6" r="4.5" fill="#fff"/></svg></span>
        <span>tobias.fyrolt</span>
      </li>
    </ul>
  </section>

</main>
</body>
</html>
```